Law Firm Website

I currently have a temporary site that I created myself at www.mcorveyfirm.net (hosted by 9tree). I am generally happy with the content.

My permanent website just has basic information right now: www.mcorveyfirm.com (hosted by lumenrack). I want to take the general content from the temporary website and have a more professional looking website on the permanent website. I want it in Wordpress format. I want a link to my blog: www.crookedpath.com. I want it to work on pads and smart phones. My number and e-mail address should be available on every page. The idea is to feature the potential client more than the lawyer.
Updates

Several of the designs are good. I would like the front page to have my number and address at the top (and at the top of every page) and to identify my law firm as "Law Office of Gerald T. Corvey". No need to include "mcorveyfirm" as that is just the web address. I like showing the most recent blog posts on the front page. I don't need video. No need to emphasize office hours or map location on the front page (that could be under a contact button). My picture should be somewhere. I would like an image from Boston on the front page if we can find one that is not copyright protected. No images of gavels or scales of justice. See some of the sample websites I listed in previous messages. Thanks!

Industry/Entity Type

Law Firm

```html
<!DOCTYPE html>
<html lang="en">
<head>
<meta charset="utf-8">
<title>Law Office of Gerald T. Corvey</title>
<link href="https://fonts.googleapis.com/css2?family=Arimo:wght@400;700&family=Noto+Serif:ital,wght@1,400;1,700&display=swap" rel="stylesheet">
<style>
:root{
  --page-bg:#161616;
  --teal:#17879a;
  --teal-dark:#0d5766;
  --teal-deep:#0a3f4b;
  --nav-bg:#0e0e0e;
  --white:#ffffff;
  --text:#333333;
  --muted:#9a9a9a;
  --heading-blue:#1c6fb0;
  --field-bg:#1d7f91;
  --footer-bg:#1e1e1e;
  --footer-line:#2f2f2f;
}
*{box-sizing:border-box;margin:0;padding:0}
html,body{width:898px;height:1200px;overflow:hidden;background:var(--page-bg)}
body{font-family:"Arimo",Arial,sans-serif;color:var(--text);position:relative}
.site{position:relative;width:898px;height:1200px}

.brand{position:absolute;left:24px;top:0;width:160px;height:128px;background:linear-gradient(180deg,var(--teal) 0%,var(--teal-dark) 100%);display:flex;align-items:center;padding-left:16px}
.brand-name{font-family:"Arimo",Arial,sans-serif;font-weight:700;font-size:25px;line-height:1.15;color:var(--white)}

.topbar{position:absolute;right:30px;top:20px;text-align:right;color:#cfcfcf}
.topbar .address{font-size:11px}
.topbar .phone{font-size:20px;color:var(--white);margin-top:12px}

.main-nav{position:absolute;left:200px;right:30px;top:118px;height:26px;background:var(--nav-bg);display:flex;align-items:center;justify-content:space-between;padding:0 10px}
.main-nav a{color:var(--white);text-decoration:none;font-size:11px;font-weight:700}

.hero{position:absolute;left:30px;right:30px;top:148px;height:210px;background:linear-gradient(180deg,#e9eef0 0%,#f7f8f8 55%,#d6dde0 100%)}

.feature{position:absolute;top:358px;height:128px;background:linear-gradient(180deg,var(--teal) 0%,var(--teal-deep) 100%);padding:10px 18px;color:var(--white)}
.feature.why{left:30px;width:413px}
.feature.expertise{left:449px;width:419px}
.feature h2{font-family:"Noto Serif",Georgia,serif;font-style:italic;font-weight:400;font-size:22px;margin-bottom:6px}
.feature p{font-size:11.5px;line-height:1.4}

.content{position:absolute;left:30px;right:30px;top:486px;height:420px;background:var(--white)}
.intro{position:absolute;left:18px;top:20px;width:540px}
.intro h1{font-size:20px;font-weight:400;line-height:1.25;color:var(--heading-blue);margin-bottom:16px}
.intro p{font-size:12px;line-height:1.45;margin-bottom:14px}
.intro .lead{width:340px}
.building{position:absolute;left:390px;top:196px;width:160px;height:92px;background:linear-gradient(135deg,#3c4e5c 0%,#8aa0ad 50%,#2c3a45 100%)}

.contact-panel{position:absolute;left:585px;top:10px;width:245px}
.contact-panel h2{font-family:"Noto Serif",Georgia,serif;font-style:italic;font-weight:400;font-size:23px;color:#222;margin-bottom:10px;border-bottom:1px solid #ddd;padding-bottom:6px}
.contact-panel p{font-size:11.5px;line-height:1.4;margin-bottom:12px}
.field{background:var(--field-bg);color:#e3f2f5;font-size:11px;height:30px;padding:9px 12px;margin-bottom:10px}
.field.message{height:100px}
.send{display:inline-block;background:var(--teal-dark);color:var(--white);font-size:11px;padding:9px 14px;margin-top:4px}

.footer{position:absolute;left:30px;right:30px;top:918px;height:150px;display:flex;gap:30px;border-bottom:1px solid var(--footer-line)}
.footer section{flex:1}
.footer h3{font-family:"Noto Serif",Georgia,serif;font-style:italic;font-weight:400;font-size:22px;color:var(--white);margin-bottom:8px}
.footer h3 span{color:var(--teal)}
.footer p{font-size:10.5px;line-height:1.5;color:#cfcfcf}

.legal{position:absolute;left:30px;right:30px;top:1080px;font-size:9px;line-height:1.5;color:var(--muted)}
</style>
</head>
<body>
<div class="site">
  <div class="brand"><span class="brand-name">Gerald T.<br>Corvey</span></div>

  <div class="topbar">
    <div class="address">18 Harbor Lane, 3rd Floor, Boston, MA 02110</div>
    <div class="phone">Call Today : 617 555-0142</div>
  </div>

  <nav class="main-nav">
    <a href="#">Home</a><a href="#">Why Hire Me?</a><a href="#">Success Stories</a><a href="#">Practice Areas</a><a href="#">Representative Clients</a><a href="#">Services Provided</a><a href="#">Contact Us</a><a href="#">How To Find Us</a>
  </nav>

  <div class="hero" role="img" aria-label="Group of smiling business professionals"></div>

  <div class="feature why">
    <h2>Why Hire Me?</h2>
    <p>I give real, practical advice to keep you out of trouble, stay in business and make money. I won't bore you with legal theories, but will explain how the legal issues affect your business.</p>
  </div>
  <div class="feature expertise">
    <h2>Expertise in Employment</h2>
    <p>I don't do everything. I don't handle personal injury claims, criminal matters, divorces, real estate transactions, bankruptcies, etc. (I can refer you to excellent lawyers who do these things).</p>
  </div>

  <main class="content">
    <div class="intro">
      <h1>Protecting and Defending Your Business Against Competitors, Rogue Employees, Cheating Business Partners, Devious Contracting Parties, and Overzealous Government Agencies.</h1>
      <p class="lead">Your business is under constant attack. With more success, you become more of a target. Whether it's keeping you out of a lawsuit or defending one that you are already in or prosecuting one when necessary, I'm here to help.</p>
      <p class="lead">Don't settle for lawyers who promise to work to solve your problems. I will work to prevent your problems in the first place. Learn more about litigation avoidance in my practice areas of law.</p>
    </div>
    <div class="building" role="img" aria-label="Glass office towers seen from below"></div>

    <aside class="contact-panel">
      <h2>Contact Us Today</h2>
      <p>If you have questions or want to make an appointment then contact us:</p>
      <div class="field">Name</div>
      <div class="field">Email</div>
      <div class="field">Phone</div>
      <div class="field message">Message</div>
      <span class="send">Send us Email</span>
    </aside>
  </main>

  <footer class="footer">
    <section>
      <h3>Contact <span>Info</span></h3>
      <p>Law Office of Gerald T. Corvey<br>18 Harbor Lane, 3rd Floor, Boston, MA 02110<br>Phone: 617 555-0142<br>Fax: 617 555-0143<br>Email: gerald@mcorveyfirm.com</p>
    </section>
    <section>
      <h3>Office <span>Hours</span></h3>
      <p>We can be reached during the following hours:<br>Monday thru Friday 10am-6pm</p>
    </section>
    <section>
      <h3>Successes</h3>
      <p>A recent study shows that plaintiffs in most diversity class actions asked a judge to "certify a class" of those covered in the suit.</p>
    </section>
  </footer>

  <div class="legal">
    <p>Copyright © 2012 Law Office of Gerald T. Corvey. All rights reserved.</p>
    <p>This site offers general information only and is not legal advice. Reading it does not form a client relationship with the firm.</p>
    <p>Past results do not guarantee a similar outcome. Please contact the office to discuss your own matter.</p>
  </div>
</div>
</body>
</html>
```